Hydraulics Company Business Card Design

Modern business card design for a hydraulics company.
Our company colours are - black, orange and white.
I would like the following contact details included-
Name
Position
Phone number
Email
Website
Street Address

I have attached our company logo.
I would like the back of the card white.

Thank you.

```html
<!DOCTYPE html>
<html lang="en">
<head>
<meta charset="utf-8">
<title>Northgate Hydraulics – Business Card</title>
<link rel="stylesheet" href="https://fonts.googleapis.com/css2?family=Montserrat:wght@500;700&display=swap">
<style>
  :root {
    --orange: #f7951d;
    --black: #141414;
    --white: #ffffff;
    --ink: #1a1a1a;
    --backdrop: #3a3a3a;
  }
  * { margin: 0; padding: 0; box-sizing: border-box; }
  html, body {
    width: 1200px; height: 694px; overflow: hidden;
    background: var(--backdrop);
    font-family: "Montserrat", Arial, sans-serif;
  }
  .canvas { position: relative; width: 1200px; height: 694px; }
  .card {
    position: absolute; top: 192px;
    width: 540px; height: 309px;
    border-radius: 18px; overflow: hidden;
  }

  /* Company name: one colour, one weight, plain square beside it */
  .brand {
    display: flex; align-items: center;
    color: var(--orange); font-weight: 700; white-space: nowrap;
  }
  .brand-square { background: var(--orange); flex: none; }

  /* Front */
  .card--front { left: 40px; background: var(--black); }
  .card--front .brand {
    position: absolute; left: 0; right: 0; top: 0; bottom: 0;
    justify-content: center; gap: 14px; font-size: 32px;
  }
  .card--front .brand-square { width: 22px; height: 22px; }

  /* Back */
  .card--back { left: 620px; background: var(--white); color: var(--ink); }
  .card--back .brand {
    position: absolute; right: 30px; top: 34px;
    gap: 10px; font-size: 20px;
  }
  .card--back .brand-square { width: 14px; height: 14px; }

  .accent-bar {
    position: absolute; left: 0; top: 112px; width: 8px; height: 60px;
    background: var(--orange);
  }
  .person { position: absolute; left: 26px; top: 116px; }
  .person-name {
    color: var(--orange); font-weight: 700; font-size: 24px; letter-spacing: 0.5px;
  }
  .person-role { font-size: 16px; font-weight: 500; margin-top: 4px; }
  .divider {
    position: absolute; left: 60px; right: 30px; top: 182px;
    height: 1.5px; background: var(--orange);
  }
  .contact { position: absolute; left: 60px; top: 196px; font-size: 14px; font-weight: 500; }
  .contact-row { display: flex; align-items: center; gap: 8px; margin-bottom: 6px; }
  .contact-row svg { width: 14px; height: 14px; fill: var(--orange); }
  .address {
    position: absolute; right: 30px; top: 196px; text-align: right;
    font-size: 14px; font-weight: 500; line-height: 1.5;
  }
  .footer-band { position: absolute; left: 0; bottom: 0; width: 540px; height: 60px; }
  .website {
    position: absolute; right: 30px; bottom: 12px;
    color: var(--white); font-size: 13px; font-weight: 500;
  }
</style>
</head>
<body>
<main class="canvas">
  <section class="card card--front" aria-label="Card front">
    <div class="brand">
      <span class="brand-square"></span>
      <span class="brand-name">Northgate Hydraulics</span>
    </div>
  </section>

  <section class="card card--back" aria-label="Card back">
    <div class="brand">
      <span class="brand-square"></span>
      <span class="brand-name">Northgate Hydraulics</span>
    </div>

    <span class="accent-bar"></span>
    <div class="person">
      <div class="person-name">DALE WHITMORE</div>
      <div class="person-role">Owner / CEO</div>
    </div>

    <span class="divider"></span>

    <div class="contact">
      <div class="contact-row">
        <svg viewBox="0 0 24 24" aria-hidden="true"><path d="M6.6 10.8a15 15 0 0 0 6.6 6.6l2.2-2.2c.3-.3.7-.4 1-.2 1.1.4 2.3.6 3.6.6.6 0 1 .4 1 1V20c0 .6-.4 1-1 1A17 17 0 0 1 3 4c0-.6.4-1 1-1h3.5c.6 0 1 .4 1 1 0 1.3.2 2.5.6 3.6.1.3 0 .7-.2 1z"/></svg>
        <span>555-214-7830</span>
      </div>
      <div class="contact-row">
        <svg viewBox="0 0 24 24" aria-hidden="true"><path d="M2 5h20v14H2z M2 5l10 8 10-8" fill="none" stroke="#f7951d" stroke-width="2.4"/></svg>
        <span>info@northgatehydraulics.com</span>
      </div>
    </div>

    <div class="address">
      27-310 Cedar Ridge Ave<br>
      Linwood, ON K0A 2C4
    </div>

    <svg class="footer-band" viewBox="0 0 540 60" aria-hidden="true">
      <path d="M0 52 H285 C300 52 300 20 318 20 H540 V60 H0 Z" fill="#f7951d"/>
      <path d="M0 56 H287 C304 56 304 24 320 24 H540 V60 H0 Z" fill="#141414"/>
    </svg>
    <div class="website">www.northgatehydraulics.com</div>
  </section>
</main>
</body>
</html>
```